PRICE LIST

I wont a design similar to my business card but not black i wont it very easy to read and simple here is my price list so far

Industry/Entity Type

Business

Font styles to use
Script

```html
<!DOCTYPE html>
<html lang="en">
<head>
<meta charset="utf-8">
<title>Simply Glow – Price List</title>
<link href="https://fonts.googleapis.com/css2?family=Lobster&family=Barlow:wght@400;500;600;700&display=swap" rel="stylesheet">
<style>
  :root {
    --ink: #111111;
    --pink: #e6007e;
    --paper: #ffffff;
    --tile: #d9d9d9;
  }
  html, body { margin: 0; padding: 0; overflow: hidden; background: var(--paper); }
  .sheet {
    position: relative; width: 846px; height: 1200px; overflow: hidden;
    background: var(--paper); color: var(--ink);
    font-family: "Barlow", Arial, sans-serif;
  }
  .brand-title {
    position: absolute; left: 78px; top: 52px; width: 724px; margin: 0;
    font-family: "Lobster", cursive; font-weight: 400;
    font-size: 128px; line-height: 1; white-space: nowrap; color: var(--ink);
  }
  .tagline {
    position: absolute; left: 0; width: 872px; top: 250px; margin: 0;
    text-align: center; font-size: 33px; font-weight: 700; letter-spacing: 0.6px;
  }
  .section-heading {
    position: absolute; margin: 0; color: var(--pink);
    font-size: 23px; font-weight: 700; letter-spacing: 0.3px;
  }
  .nails-heading { left: 84px; top: 338px; }
  .wax-heading { left: 525px; top: 340px; }
  .tan-heading { left: 590px; top: 720px; }

  .nail-menu { position: absolute; left: 80px; top: 385px; width: 330px; }
  .nail-item { position: absolute; right: 0; width: 330px; }
  .nail-name {
    position: absolute; right: 55px; font-size: 16px; font-weight: 700; white-space: nowrap;
  }
  .nail-price { position: absolute; left: 293px; font-size: 16px; font-weight: 700; }
  .nail-desc {
    position: absolute; right: 55px; width: 300px; margin: 0; text-align: right;
    font-size: 16px; line-height: 20px; font-weight: 400;
  }

  .wax-menu { position: absolute; left: 525px; top: 390px; margin: 0; padding: 0; list-style: none; }
  .wax-item { display: flex; width: 230px; height: 31px; font-size: 16px; font-weight: 700; }
  .wax-item .wax-name { width: 199px; }

  .partner-name {
    position: absolute; left: 520px; top: 622px; width: 260px; text-align: center;
    font-size: 34px; font-weight: 700; line-height: 1; color: var(--ink);
  }

  .tan-name {
    position: absolute; left: 455px; top: 805px; width: 210px; text-align: center;
    font-size: 34px; font-weight: 700; line-height: 1; color: var(--ink);
  }
  .tan-offer {
    position: absolute; left: 689px; top: 768px; width: 150px; margin: 0;
    font-size: 15px; line-height: 20px; font-weight: 700; white-space: nowrap;
  }

  .social-handle {
    position: absolute; left: 418px; top: 958px; font-size: 21px; font-weight: 700; color: var(--pink);
  }
  .social-tile {
    position: absolute; left: 680px; top: 924px; width: 90px; height: 90px;
    border-radius: 16px; background: var(--tile);
  }
  .social-dot {
    position: absolute; left: 492px; top: 1075px; width: 84px; height: 84px;
    border-radius: 50%; background: var(--tile);
  }
  .social-page {
    position: absolute; left: 612px; top: 1082px; margin: 0;
    font-size: 24px; line-height: 30px; font-weight: 700; color: var(--pink);
  }

  .contact { position: absolute; left: 76px; top: 958px; font-style: normal; }
  .contact-name { margin: 0; font-size: 56px; font-weight: 700; line-height: 1; color: var(--pink); letter-spacing: 1px; }
  .contact-phone { margin: 2px 0 4px; font-size: 30px; line-height: 40px; font-weight: 700; color: var(--pink); letter-spacing: 0.5px; }
  .contact-line { margin: 0; font-size: 23px; line-height: 38px; font-weight: 700; letter-spacing: 0.4px; }
</style>
</head>
<body>
<main class="sheet">
  <h1 class="brand-title">Simply Glow</h1>
  <p class="tagline">QUALIFIED BEAUTY THERAPIST&nbsp; FROM HOME</p>

  <h2 class="section-heading nails-heading">MANICURES &amp; PEDICURES</h2>
  <section class="nail-menu">
    <div class="nail-item" style="top:0">
      <span class="nail-name">Gel Manicure</span><span class="nail-price">$30</span>
      <p class="nail-desc" style="top:36px">Cut, shape, cuticles &amp; Gel</p>
    </div>
    <div class="nail-item" style="top:68px">
      <span class="nail-name">Deluxe Manicure</span><span class="nail-price">$40</span>
      <p class="nail-desc" style="top:30px">Soak, exfoliate, cut, shape, cuticles<br>&amp; polish or add gel for $10</p>
    </div>
    <div class="nail-item" style="top:148px">
      <span class="nail-name">Paraffin Manicure</span><span class="nail-price">$45</span>
      <p class="nail-desc" style="top:30px">Soak, exfoliate, paraffin treatment.<br>Cut, shape, cuticles<br>&amp; polish or add gel for $5’</p>
    </div>
    <div class="nail-item" style="top:249px">
      <span class="nail-name">Gel Pedicure</span><span class="nail-price">$30</span>
      <p class="nail-desc" style="top:30px">Cut, shape, cuticles &amp; Gel</p>
    </div>
    <div class="nail-item" style="top:310px">
      <span class="nail-name">Deluxe Pedicure</span><span class="nail-price">$40</span>
      <p class="nail-desc" style="top:30px">Soak, exfoliate, cut, shape, cuticles<br>&amp; polish or add gel for $10’</p>
    </div>
    <div class="nail-item" style="top:390px">
      <span class="nail-name">Paraffin Pedicure</span><span class="nail-price">$45</span>
      <p class="nail-desc" style="top:32px">Soak, exfoliate, paraffin treatment,<br>cut, shape, cuticles &amp; polish or add<br>gel for $5’</p>
    </div>
  </section>

  <h2 class="section-heading wax-heading">WAXING &amp; TINTING</h2>
  <ul class="wax-menu">
    <li class="wax-item"><span class="wax-name">Eyebrow Wax</span><span>$10</span></li>
    <li class="wax-item"><span class="wax-name">Eyebrow Tint</span><span>$10</span></li>
    <li class="wax-item"><span class="wax-name">Eyelash Tint</span><span>$10</span></li>
    <li class="wax-item"><span class="wax-name">Lip Wax</span><span>$10</span></li>
    <li class="wax-item"><span class="wax-name">Chin Wax</span><span>$10</span></li>
    <li class="wax-item"><span class="wax-name">Underarm</span><span>$15</span></li>
  </ul>

  <div class="partner-name">Polara</div>

  <h2 class="section-heading tan-heading">TANNING</h2>
  <div class="tan-name">SunMist</div>
  <p class="tan-offer">The very popular<br>“2 Hour SUNMIST<br>TAN” in all<br>ranges is now<br>available for<br>$25.00!</p>

  <span class="social-handle">simplyglowsuncoast</span>
  <span class="social-tile"></span>
  <span class="social-dot"></span>
  <p class="social-page">Simply Glow<br>Sun Coast</p>

  <address class="contact">
    <p class="contact-name">MARLEY</p>
    <p class="contact-phone">0412 345 678</p>
    <p class="contact-line">LOCATED IN MARLIN</p>
    <p class="contact-line">WATERS , SUN COAST</p>
    <p class="contact-line">FLEXIBLY HOURS 7 DAYS A WEEK</p>
  </address>
</main>
</body>
</html>
```